Real Estate Investor needs awesome business card design

I invest in real estate, focused on multi-family properties, and I need a business card to hand out to potential partners. I prefer simple, clean designs, but it needs to stand out, so I'd like there to be a bit of red in the design as well.

It should include this information:

Front
Dallin Pecksworth
Real Estate Investor
Direct phone: 502-867-3394
Email: dallinhpecksworth@quillmail.example
Headshot (Picture), I've uploaded a few, just pick the one you think looks best with your design. You can remove the background from the headshot image if it looks better.

Back
The back of the card's design should flow and be congruent with the front. On the back I want to put an inspirational quote or question. There will be different ones depending on the card, so I'll need the original file so I can edit it in the end.

For now, use “The Pessimist Sees Difficulty In Every Opportunity. The Optimist Sees The Opportunity In Every Difficulty.” -Barnaby Ellsworth

Target Market(s)

Investors

Industry/Entity Type

Real Estate

Contact Information for Business Card

Front
Dallin Pecksworth
Real Estate Investor

Back
The back of the card's design should flow and be congruent with the front. On the back I want to put an inspirational quote or question. There will be different ones depending on the card, so I'll need the original file so I can edit it in the end. I've uploaded some EXAMPLES of business cards with quotes on them. Don't copy but feel free to use them as inspiration.

The design will be printed on "ZIB sized" business cards
1039 x 697 pixels
with rounded corners

Font styles to use
Serif
Decorative
Script

Colors
ec1f27

Requirements
Must have
• Headshot, name, and other information in it.
• 1039 x 697 pixels
• Rounded corners
• Clean design that pops. I'm open to see any color background, including black.
• Headshots can be located here: https://www.filecrate.example/sh/8kd2wq7mzt31hvx/BBQTXP4ruf9LmQ0KhcvWx7b?dl=0
Nice to have
• It would be awesome if the design included a personal signature or monogram, but if not I'll get a personal logo developed later and the card redesigned if I think it needs it.
Should not have
• Cluttered design

```html
<!DOCTYPE html>
<html lang="en">
<head>
<meta charset="utf-8">
<title>Dallin Pecksworth — Business Card</title>
<link rel="stylesheet" href="https://fonts.googleapis.com/css2?family=Montserrat:wght@300;500;700&family=Roboto+Condensed:wght@700;800&display=swap">
<style>
  :root {
    --stage: #e9ebec;
    --card-black: #141414;
    --photo-light: #8a8a8a;
    --photo-mid: #4a4a4a;
    --photo-dark: #222222;
    --band: rgba(0, 0, 0, 0.68);
    --white: #ffffff;
    --soft-white: #d8d8d8;
    --red: #d1272c;
    --ink: #3b1414;
    --yellow: #f7e31b;
  }
  * { box-sizing: border-box; margin: 0; padding: 0; }
  html, body {
    width: 1200px; height: 814px; overflow: hidden;
    background: var(--stage);
  }
  .stage {
    position: relative; width: 1200px; height: 814px;
    display: flex; align-items: center; justify-content: center; gap: 40px;
  }
  .card {
    position: relative; width: 540px; height: 362px;
    border-radius: 16px; overflow: hidden;
    box-shadow: 0 10px 30px rgba(0,0,0,0.18);
  }

  /* Front */
  .card-front { background: var(--card-black); }
  .headshot {
    position: absolute; top: 0; right: 0; width: 330px; height: 100%;
    background:
      radial-gradient(ellipse 32% 34% at 38% 30%, var(--photo-light), transparent 75%),
      radial-gradient(ellipse 70% 45% at 55% 85%, var(--photo-mid), transparent 80%),
      linear-gradient(90deg, var(--card-black) 0%, var(--photo-dark) 22%, #2e2e2e 100%);
  }
  .identity {
    position: absolute; left: 28px; top: 96px;
    display: flex; align-items: flex-start; gap: 12px;
  }
  .identity-square {
    width: 16px; height: 16px; background: var(--white); margin-top: 9px;
    flex: none;
  }
  .identity-name {
    font-family: "Montserrat", sans-serif; font-weight: 300;
    color: var(--white); font-size: 34px; letter-spacing: 0.04em;
    text-transform: uppercase; line-height: 1.05;
  }
  .identity-title {
    font-family: "Montserrat", sans-serif; font-weight: 300;
    color: var(--soft-white); font-size: 14px; letter-spacing: 0.04em;
    margin-top: 8px;
  }
  .contact-band {
    position: absolute; left: 0; right: 0; bottom: 0; height: 80px;
    background: var(--band);
    display: flex; flex-direction: column; justify-content: center; align-items: flex-end;
    padding-right: 22px; gap: 6px;
  }
  .contact-phone, .contact-email {
    font-family: "Montserrat", sans-serif; font-weight: 500;
    color: var(--white); font-size: 17px;
  }
  .contact-phone { letter-spacing: 0.02em; }

  /* Back */
  .card-back { background: var(--red); }
  .quote-mark {
    position: absolute;
    font-family: "Roboto Condensed", sans-serif; font-weight: 800;
    color: var(--white); font-size: 96px; line-height: 1;
  }
  .quote-open { left: 24px; top: 14px; }
  .quote-close { right: 30px; top: 14px; }
  .quote {
    position: absolute; left: 66px; top: 44px;
    font-family: "Roboto Condensed", sans-serif; font-weight: 800;
    font-size: 36px; line-height: 0.98; color: var(--white);
  }
  .quote .dark { color: var(--ink); }
  .quote .gold { color: var(--yellow); }
  .quote-author {
    position: absolute; left: 132px; top: 276px;
    font-family: "Montserrat", sans-serif; font-weight: 500;
    color: var(--yellow); font-size: 12px; letter-spacing: 0.06em;
    text-transform: uppercase;
  }
</style>
</head>
<body>
<main class="stage">
  <section class="card card-front">
    <div class="headshot" role="img" aria-label="Black and white headshot of the investor in a dark patterned shirt"></div>
    <div class="identity">
      <span class="identity-square"></span>
      <div>
        <p class="identity-name">Dallin<br>Pecksworth</p>
        <p class="identity-title">Real Estate Investor</p>
      </div>
    </div>
    <div class="contact-band">
      <p class="contact-phone">502-867-3394</p>
      <p class="contact-email">dallinhpecksworth@quillmail.example</p>
    </div>
  </section>

  <section class="card card-back">
    <span class="quote-mark quote-open">&ldquo;</span>
    <span class="quote-mark quote-close">&rdquo;</span>
    <p class="quote">
      The <span class="dark">Pessimist Sees</span><br>
      <span class="dark">Difficulty In Every</span><br>
      <span class="dark">Opportunity</span>. The<br>
      <span class="gold">Optimist</span> Sees The<br>
      <span class="gold">Opportunity</span> In<br>
      Every <span class="gold">Difficulty.</span>
    </p>
    <p class="quote-author">Barnaby Ellsworth</p>
  </section>
</main>
</body>
</html>
```